Web Portal Design for Velmoto – Subcontractor Verification Platform

Velmoto is a European startup focused on verifying and confirming the identity of subcontractors in the transport and logistics industry to prevent fraud.
The platform’s main functions include:
Company verification – confirming the legitimacy and registration details of transport companies.
Identity verification – authenticating the identity of the person registering the company and associated drivers.
Geo-zone monitoring – a unique mobile feature that allows the creation of geo-fenced areas at loading locations. This enables verification and tracking of who is actually present and authorized to collect the goods.
Safe subcontracting visibility – full transparency of subcontracting chains, ensuring each level of cooperation remains verified and secure.
In short, Velmoto helps build secure subcontractor networks for both shippers and freight forwarders.
I have already created a basic website using Framer, but I am not fully satisfied with the current design and graphic quality. I’m looking for a professional designer who can help improve the UI/UX, visual consistency, and overall aesthetics of the portal to better reflect our innovative and security-focused mission.
Design Style & Colors:
Modern, minimalistic layout
Primary colors: gray, white, and black
Accent color: green (for highlights, buttons, and trust indicators)
Clean typography and intuitive structure
Preference for a professional, tech-oriented look that conveys trust, security, and innovation
The website must definitely include the option to book a demo and provide information about pricing models, which should be easy to edit. There should also be an option to purchase subscriptions directly through the website. There will be three pricing models.
My project should serve as your inspiration, not a template — I’m not expecting it to look identical. We’re looking for something unique and truly “wow.”
Updates
Low design quality
We are looking for a contractor to design and develop a website for the modern application Velmoto, focused on identity verification in the logistics and transport industry. The website will serve as a branding and sales tool, presenting the innovation, security, and professionalism of our solution.
We are not interested in ready-made templates – we expect a fully custom, unique design tailored to the nature of the product and the TSL market.
Velmoto is an advanced platform for verifying the identity of companies, drivers, and subcontractors in logistics. Our goal is to eliminate fraud, theft, and impersonation of legitimate carriers through:
digital identity verification
subcontractor authorisation
creation of trusted company lists
increasing supply chain security
The website should clearly communicate: security, technology, trust, and innovation.
Design Requirements
Style & Design
No ready-made templates
Modern, technology-driven appearance
Premium / corporate-tech aesthetic
Minimalist, clean layout with clear content hierarchy
Colour Scheme
Existing graphics in green tones (we provide our own materials)
Website background: grey or dark (graphite, dark anthracite, deep grey)
Contrasting elements for CTAs and key sections
Industry Focus
Logistics / Transport / Digital Security
Visual identity should evoke:
trust
control
technology
data protection
The website must allow:
easy content editing
independent updating of texts and images without developer involvement
full responsiveness (desktop, tablet, mobile)
fast loading performance
SEO-ready structure
Target Market(s)
Producers
Coding
Number of Pages Required
1 page
Look and feel

```html
<!DOCTYPE html>
<html lang="en">
<head>
<meta charset="utf-8">
<title>Velmoto – Trusted transport starts here</title>
<link rel="stylesheet" href="https://fonts.googleapis.com/css2?family=Urbanist:wght@400;500;600;700;800&display=swap">
<style>
:root{
  --white:#ffffff;
  --ink:#111111;
  --text:#3d3d3d;
  --muted:#6b6b6b;
  --line:#e4e6e8;
  --card:#f6f7f8;
  --graphite:#4a4a4a;
  --graphite-deep:#333333;
  --green:#6bb874;
  --green-dark:#4f9d59;
}
*{box-sizing:border-box;margin:0;padding:0}
html,body{width:1200px;height:3326px;overflow:hidden}
body{position:relative;background:var(--white);font-family:"Urbanist",sans-serif;color:var(--ink)}
.abs{position:absolute}
a{color:inherit;text-decoration:none}

/* nav */
.site-nav{position:absolute;left:0;top:0;width:1200px;height:79px;border-bottom:1px solid var(--line)}
.brand{position:absolute;left:106px;top:22px;font-size:30px;font-weight:700;letter-spacing:-0.5px;display:flex;align-items:center;gap:6px}
.brand-dot{width:10px;height:10px;border:1.5px solid var(--ink);border-radius:50%}
.nav-links{position:absolute;left:460px;top:31px;display:flex;gap:34px;font-size:13px;font-weight:500}
.sign-in{position:absolute;left:924px;top:31px;font-size:13px;font-weight:700}
.btn{display:inline-flex;align-items:center;justify-content:center;border-radius:30px;font-weight:700;font-size:13px}
.btn-green{background:var(--green);color:var(--white)}
.btn-outline{border:1.5px solid var(--ink);color:var(--ink);background:var(--white)}
.nav-demo{position:absolute;left:973px;top:19px;width:121px;height:40px}

/* hero */
.release-badge{position:absolute;left:107px;top:204px;width:287px;height:37px;border:1px solid var(--line);border-radius:20px;display:flex;align-items:center;gap:8px;padding-left:20px;font-size:11px;color:var(--text)}
.release-badge span{color:var(--green-dark)}
.hero-title{position:absolute;left:106px;top:252px;font-size:47px;font-weight:700;line-height:1.05;letter-spacing:-1.2px}
.hero-copy{position:absolute;left:107px;top:366px;width:430px;font-size:14.5px;line-height:1.4;color:var(--text)}
.hero-watch{left:107px;top:473px;width:160px;height:41px;gap:8px}
.hero-start{left:275px;top:473px;width:121px;height:41px}
.hero-art{left:594px;top:142px;width:503px;height:503px;border-radius:20px;background:radial-gradient(circle at 50% 50%,#f2f4f2 0%,#ffffff 75%)}

/* automate */
.automate{position:absolute;left:0;top:711px;width:1200px;height:547px;overflow:hidden;background:linear-gradient(180deg,var(--graphite) 0%,var(--graphite-deep) 100%)}
.automate-circle{position:absolute;left:165px;top:340px;width:380px;height:380px;border-radius:50%;background:#5a5a5a}
.automate-art{position:absolute;left:71px;top:50px;width:568px;height:423px;border-radius:14px;background:linear-gradient(135deg,rgba(255,255,255,.14),rgba(255,255,255,.05))}
.automate-title{position:absolute;left:722px;top:106px;font-size:41px;font-weight:600;line-height:1.2;color:var(--white);letter-spacing:-0.8px}
.automate-copy{position:absolute;left:722px;top:273px;width:345px;font-size:14.5px;line-height:1.4;color:#e8e8e8}
.automate-demo{left:721px;top:402px;width:122px;height:39px}

/* tools */
.section-title{position:absolute;left:0;width:1200px;text-align:center;font-size:46px;font-weight:600;line-height:1.08;letter-spacing:-1.2px}
.section-sub{position:absolute;left:0;width:1200px;text-align:center;font-size:14.5px;line-height:1.4;color:var(--text)}
.tool-card{position:absolute;background:var(--card);border:1px solid var(--line);border-radius:22px}
.tool-card .art{position:absolute;left:30px;right:30px;top:24px;border-bottom:1px solid #cfd3d6;background:linear-gradient(180deg,#eef0f2,#f6f7f8)}
.tool-card h3{position:absolute;left:30px;font-size:18px;font-weight:600;letter-spacing:-0.3px}
.tool-card p{position:absolute;left:30px;right:26px;font-size:11.5px;line-height:1.3;color:var(--text)}

/* pricing */
.plan{position:absolute;border-radius:14px;background:var(--white);box-shadow:0 10px 40px rgba(0,0,0,.08)}
.plan-name{position:absolute;left:0;right:0;top:20px;text-align:center;font-size:17px;font-weight:700;line-height:24px}
.plan-rule{position:absolute;left:25px;right:25px;top:54px;height:1px;background:var(--line)}
.plan-price{position:absolute;left:0;right:0;top:64px;text-align:center;font-size:38px;font-weight:700;line-height:46px}
.plan-per{position:absolute;left:0;right:0;top:110px;text-align:center;font-size:12px;line-height:16px;color:var(--text)}
.plan-list{position:absolute;left:25px;right:25px;top:137px;list-style:none}
.plan-list li{display:flex;align-items:center;gap:6px;height:30px;font-size:11.5px;line-height:1;border-bottom:1px solid var(--line)}
.plan-list li:last-child{border-bottom:none}
.tick{width:9px;height:9px;border-radius:50%;background:var(--green);flex:none}
.plan-btn{position:absolute;left:42px;right:42px;height:38px;font-size:11px;letter-spacing:.3px}
.plan-pro{background:linear-gradient(180deg,#4e4e4e,#2f2f2f);color:var(--white);box-shadow:0 16px 40px rgba(0,0,0,.2)}
.plan-pro .plan-list li{border-color:#5e5e5e}
.plan-pro .plan-rule{background:#5e5e5e}
.plan-pro .plan-per{color:#dcdcdc}
.popular{position:absolute;right:0;top:24px;background:#6e6e6e;color:var(--white);font-size:9px;font-weight:700;padding:5px 10px;border-radius:10px 0 0 10px}

/* marquee */
.marquee{position:absolute;left:-8px;top:2938px;white-space:nowrap;font-size:90px;font-weight:500;color:transparent;-webkit-text-stroke:1.3px #c9cbcd;letter-spacing:-1px;line-height:1}
.marquee b{color:#333;-webkit-text-stroke:0;font-weight:700;font-size:60px;vertical-align:10px;margin:0 30px}

/* footer */
.site-footer{position:absolute;left:0;top:3016px;width:1200px;height:310px;background:linear-gradient(180deg,var(--graphite-deep),#4a4a4a);color:var(--white)}
.footer-brand{position:absolute;left:0;width:1200px;top:62px;text-align:center;font-size:86px;font-weight:700;letter-spacing:-2px;line-height:1}
.footer-links{position:absolute;left:0;width:1200px;top:168px;display:flex;justify-content:center;gap:34px;font-size:13px}
.footer-rule{position:absolute;left:106px;right:106px;top:251px;height:1px;background:#6a6a6a}
.copyright{position:absolute;left:0;width:1200px;top:275px;text-align:center;font-size:12.5px}
.to-top{position:absolute;left:1127px;top:235px;width:32px;height:32px;border-radius:50%;background:var(--white);display:flex;align-items:center;justify-content:center}
</style>
</head>
<body>

<header class="site-nav">
  <a class="brand" href="#">Velmoto<i class="brand-dot"></i></a>
  <nav class="nav-links"><a href="#">Features</a><a href="#">Pricing</a><a href="#">Blog</a><a href="#">Changelog</a></nav>
  <a class="sign-in" href="#">Sign In</a>
  <a class="btn btn-green nav-demo" href="#">Book a Demo</a>
</header>

<section class="hero">
  <div class="release-badge">
    <svg width="12" height="12" viewBox="0 0 12 12"><path d="M6 0l1.4 4.6L12 6 7.4 7.4 6 12 4.6 7.4 0 6l4.6-1.4z" fill="#222"/></svg>
    We released V2 open API <span>See changelog ↗ ›</span>
  </div>
  <h1 class="hero-title">Trusted transport<br>starts here</h1>
  <p class="hero-copy">At Velmoto, we're building a new standard for security and verification intelligence for logistics-creating an environment where every connection is verified, every process is transparent, and every partner can operate with complete confidence.</p>
  <a class="btn btn-outline abs hero-watch" href="#"><svg width="9" height="10" viewBox="0 0 9 10"><path d="M0 0l9 5-9 5z" fill="#111"/></svg>See how it works</a>
  <a class="btn btn-green abs hero-start" href="#">Start For Free</a>
  <div class="abs hero-art" role="img" aria-label="Illustrated verification journey: warehouse, trucks, freight exchange and verified subcontracting chain around the Velmoto platform"></div>
</section>

<section class="automate">
  <div class="automate-circle"></div>
  <div class="automate-art" role="img" aria-label="Workflow diagram of verification steps: company finder, company check, approved drivers, geofenced plant and gate portal"></div>
  <h2 class="automate-title">Optimise &amp; automate<br>your verification<br>processes</h2>
  <p class="automate-copy">Turn the complex and time-consuming verification process into a smooth, automated workflow. Velmoto empowers shippers, manufacturers, warehouses and forwarders to work smarter, safer and faster than ever before.</p>
  <a class="btn btn-green abs automate-demo" href="#">Book a Demo</a>
</section>

<section class="tools">
  <h2 class="section-title" style="top:1352px">All your verification tools<br>in one simple platform</h2>
  <p class="section-sub" style="top:1466px">Subcontracting doesn't have to be risky - it can open up new opportunities.<br>Create the perfect mix of tools to protect your business.</p>

  <article class="tool-card" style="left:105px;top:1564px;width:326px;height:622px">
    <div class="art" style="height:440px;border-bottom:none;background:linear-gradient(180deg,#f0f2f1,#f6f7f8)" role="img" aria-label="Illustration of a verified network of warehouses, carriers and trucks"></div>
    <h3 style="top:490px">Your unique network</h3>
    <p style="top:525px">Create and manage your own network of verified partners-carriers, drivers, &amp; loading points. Control who gains access to your operations, prevent unauthorized entries, &amp; get instant notifications.</p>
  </article>

  <article class="tool-card" style="left:444px;top:1564px;width:319px;height:305px">
    <div class="art" style="height:152px" role="img" aria-label="Illustration of a driver identity check on a phone"></div>
    <h3 style="top:173px">You know who you work with</h3>
    <p style="top:208px">Verifies every company, employee, and driver through a secure, AI-powered process. Work only with trusted partners - verified in minutes, accessible through one simple app.</p>
  </article>

  <article class="tool-card" style="left:774px;top:1564px;width:320px;height:305px">
    <div class="art" style="height:152px" role="img" aria-label="Illustration of a geofenced loading site with warehouse and trucks"></div>
    <h3 style="top:173px">Smart Access &amp; Location</h3>
    <p style="top:208px">Access to loading sites or release of loading ref is granted only after a verified driver enters the defined geozone. Create fixed loading zones or define them individually for each order.</p>
  </article>

  <article class="tool-card" style="left:444px;top:1880px;width:319px;height:306px">
    <div class="art" style="height:152px" role="img" aria-label="Illustration of a transparent subcontracting chain"></div>
    <h3 style="top:173px">No hidden subcontracting</h3>
    <p style="top:208px">Even if your order is passed down the chain, we give you full visibility of who actually executes the job-and notify you instantly if an issue occurs</p>
  </article>

  <article class="tool-card" style="left:774px;top:1880px;width:320px;height:306px">
    <div class="art" style="height:152px" role="img" aria-label="Illustration of API-connected gate management"></div>
    <h3 style="top:173px">Loading Gate Management</h3>
    <p style="top:208px">Standardize gate operations-no longer need to manually check documents. Velmoto automates the entire loading access process.</p>
  </article>
</section>

<section class="pricing">
  <h2 class="section-title" style="top:2278px">Our pricing plans</h2>

  <div class="plan" style="left:237px;top:2396px;width:243px;height:400px">
    <div class="plan-name">Starter</div><div class="plan-rule"></div>
    <div class="plan-price">$0</div><div class="plan-per">Per month</div>
    <ul class="plan-list">
      <li><i class="tick"></i>Up to 50 verifications</li><li><i class="tick"></i>Email Support</li><li><i class="tick"></i>Basic Analytics</li>
      <li><i class="tick"></i>Up to 50 verifications</li><li><i class="tick"></i>Email Support</li><li><i class="tick"></i>Basic Analytics</li>
    </ul>
    <a class="btn btn-outline plan-btn" style="top:332px" href="#">CHOOSE PLAN</a>
  </div>

  <div class="plan" style="left:720px;top:2396px;width:243px;height:400px">
    <div class="plan-name">Enterprise</div><div class="plan-rule"></div>
    <div class="plan-price">$99</div><div class="plan-per">Per month</div>
    <ul class="plan-list">
      <li><i class="tick"></i>Unlimited verifications</li><li><i class="tick"></i>Dedicated Account Manager</li><li><i class="tick"></i>API Access</li>
      <li><i class="tick"></i>Unlimited verifications</li><li><i class="tick"></i>Dedicated Account Manager</li><li><i class="tick"></i>API Access</li>
    </ul>
    <a class="btn btn-outline plan-btn" style="top:332px" href="#">CHOOSE PLAN</a>
  </div>

  <div class="plan plan-pro" style="left:479px;top:2365px;width:242px;height:453px">
    <span class="popular">MOST POPULAR</span>
    <div class="plan-name" style="top:51px">Pro Plan</div><div class="plan-rule" style="top:85px"></div>
    <div class="plan-price" style="top:95px">$29</div><div class="plan-per" style="top:141px">Per month</div>
    <ul class="plan-list" style="top:168px">
      <li><i class="tick"></i>Up to 200 verifications</li><li><i class="tick"></i>Priority Support</li><li><i class="tick"></i>Advanced Reporting</li>
      <li><i class="tick"></i>Up to 200 verifications</li><li><i class="tick"></i>Priority Support</li><li><i class="tick"></i>Advanced Reporting</li>
    </ul>
    <a class="btn btn-green plan-btn" style="top:363px" href="#">CHOOSE PLAN</a>
  </div>
</section>

<div class="marquee">etwork<b>*</b>Management<b>*</b>Location</div>

<footer class="site-footer">
  <div class="footer-brand">Velmoto</div>
  <nav class="footer-links"><a href="#">Features</a><a href="#">Pricing</a><a href="#">Blog</a><a href="#">Changelog</a></nav>
  <a class="to-top" href="#" aria-label="Back to top"><svg width="10" height="6" viewBox="0 0 10 6"><path d="M1 5l4-4 4 4" stroke="#333" stroke-width="1.5" fill="none"/></svg></a>
  <div class="footer-rule"></div>
  <p class="copyright">© Copyright 2025 Velmoto All Rights Reserved</p>
</footer>

</body>
</html>
```